Business Card Design

I need a business card for company that is a limited company that was originally an off-road vehicle company (atv's side by sides snowmobiles and motorcycles) and I have recently sold the assets of the company that was operating under a different name and have become semi retired. I continue to do maintenance on these types of vehicles and also sell and install parts and accessories. Recently I have also contracted to a snowmobile club to operate their groomer to groom the snowmobile trails. I would like bright and bold colors.
Industry/Entity Type
Club
Contact Information for Business Card
KWT Holdings Ltd.
Marcus Ellery
780-555-0143

```html
<!DOCTYPE html>
<html lang="en">
<head>
<meta charset="utf-8">
<title>KWT Holdings Ltd. – Business Card</title>
<link href="https://fonts.googleapis.com/css2?family=Michroma&display=swap" rel="stylesheet">
<style>
  :root {
    --card-white: #ffffff;
    --band-red: #e0141b;
    --logo-grey: #a7a9a9;
    --text-white: #ffffff;
    --contact-red: #e3161d;
    --badge-green: #2fa33a;
    --tick-grey: #d9d9d9;
  }
  html, body {
    margin: 0;
    padding: 0;
    width: 1200px;
    height: 702px;
    overflow: hidden;
    background: var(--card-white);
  }
  .card {
    position: relative;
    width: 1200px;
    height: 702px;
    background: var(--card-white);
    font-family: "Michroma", sans-serif;
    overflow: hidden;
  }
  .red-band {
    position: absolute;
    left: 59px; top: 56px;
    width: 1086px; height: 432px;
    background: var(--band-red);
    overflow: hidden;
  }
  .services {
    position: absolute;
    left: 32px; top: 124px;
    color: var(--text-white);
  }
  .services__title {
    margin: 0 0 26px;
    font-size: 18px;
    font-weight: 400;
    letter-spacing: 0.5px;
    text-transform: uppercase;
  }
  .services__list {
    list-style: none;
    margin: 0; padding: 0 0 0 8px;
  }
  .services__item {
    display: flex;
    align-items: flex-start;
    margin-bottom: 27px;
    font-size: 15px;
    letter-spacing: 1.5px;
    text-transform: uppercase;
    line-height: 33px;
  }
  .services__tick {
    flex: none;
    width: 34px; height: 34px;
    margin-right: 32px;
  }
  .brand {
    position: absolute;
    left: 510px; top: 61px;
    width: 600px;
    text-align: center;
    margin: 0;
    color: var(--logo-grey);
    font-size: 36px;
    font-weight: 400;
    letter-spacing: 1px;
    line-height: 66px;
    white-space: nowrap;
  }
  .owner {
    position: absolute;
    left: 480px; top: 212px;
    width: 620px;
    text-align: center;
    color: var(--text-white);
  }
  .owner__name {
    margin: 0 0 18px;
    font-size: 25px;
    font-weight: 400;
    letter-spacing: 1.5px;
    text-transform: uppercase;
  }
  .owner__bio {
    margin: 0;
    font-size: 10.5px;
    letter-spacing: 0.8px;
    line-height: 23px;
    text-transform: uppercase;
  }
  .vehicle {
    position: absolute;
  }
  .vehicle--snowmobile {
    left: 116px; top: 516px; width: 117px; height: 80px;
    border-radius: 30% 45% 20% 20%;
    background: linear-gradient(160deg, #e23a22, #b71c1c 60%, #333 100%);
  }
  .vehicle--motorcycle {
    left: 299px; top: 527px; width: 116px; height: 62px;
    border-radius: 40% 40% 30% 30%;
    background: linear-gradient(170deg, #f07a1c, #e05a10 55%, #222 100%);
  }
  .contact {
    position: absolute;
    left: 718px; top: 530px;
    margin: 0; padding: 0;
    list-style: none;
  }
  .contact__item {
    display: flex;
    align-items: center;
    height: 30px;
    margin-bottom: 10px;
    color: var(--contact-red);
    font-size: 19px;
    letter-spacing: 1.5px;
  }
  .contact__item--email { font-size: 17px; }
  .contact__badge {
    flex: none;
    width: 30px; height: 30px;
    margin-right: 26px;
  }
</style>
</head>
<body>
<main class="card">
  <section class="red-band">
    <div class="services">
      <h2 class="services__title">Snowmobile &amp; Motorcycle</h2>
      <ul class="services__list">
        <li class="services__item">
          <svg class="services__tick" viewBox="0 0 34 34" aria-hidden="true"><rect x="2" y="8" width="22" height="22" fill="none" stroke="var(--tick-grey)" stroke-width="2"/><path d="M7 18 L13 25 L31 3" fill="none" stroke="var(--tick-grey)" stroke-width="5" stroke-linecap="round" stroke-linejoin="round"/></svg>
          Maintenance
        </li>
        <li class="services__item">
          <svg class="services__tick" viewBox="0 0 34 34" aria-hidden="true"><rect x="2" y="8" width="22" height="22" fill="none" stroke="var(--tick-grey)" stroke-width="2"/><path d="M7 18 L13 25 L31 3" fill="none" stroke="var(--tick-grey)" stroke-width="5" stroke-linecap="round" stroke-linejoin="round"/></svg>
          Selling
        </li>
        <li class="services__item">
          <svg class="services__tick" viewBox="0 0 34 34" aria-hidden="true"><rect x="2" y="8" width="22" height="22" fill="none" stroke="var(--tick-grey)" stroke-width="2"/><path d="M7 18 L13 25 L31 3" fill="none" stroke="var(--tick-grey)" stroke-width="5" stroke-linecap="round" stroke-linejoin="round"/></svg>
          <span>Install parts<br>and accessories</span>
        </li>
      </ul>
    </div>

    <h1 class="brand">KWT Holdings Ltd.</h1>

    <div class="owner">
      <h2 class="owner__name">Marcus Ellery</h2>
      <p class="owner__bio">I am a journeyman red seal automotive technician<br>journeyman red seal motorcycle technician<br>and journeyman parts man.</p>
    </div>
  </section>

  <div class="vehicle vehicle--snowmobile" role="img" aria-label="Photo of a red snowmobile"></div>
  <div class="vehicle vehicle--motorcycle" role="img" aria-label="Photo of an orange sport motorcycle"></div>

  <ul class="contact">
    <li class="contact__item">
      <svg class="contact__badge" viewBox="0 0 30 30" aria-hidden="true"><path d="M15 1 L28 8 L28 18 L15 29 L2 18 L2 8 Z" fill="var(--contact-red)"/><text x="15" y="20" text-anchor="middle" font-family="Arial, sans-serif" font-size="14" font-weight="700" fill="#fff">T</text></svg>
      780-555-0143
    </li>
    <li class="contact__item contact__item--email">
      <svg class="contact__badge" viewBox="0 0 30 30" aria-hidden="true"><path d="M15 1 L28 8 L28 18 L15 29 L2 18 L2 8 Z" fill="var(--badge-green)"/><text x="15" y="20" text-anchor="middle" font-family="Arial, sans-serif" font-size="14" font-weight="700" fill="#fff">E</text></svg>
      kwtholdings.22@mail.com
    </li>
  </ul>
</main>
</body>
</html>
```